Photographer website

This website will contain information to sell the services of marvento quillas an up and coming photographer based in london
Updates

Target Market(s)

SME's for corporate head shots
mums for kids parties
actors - for headshots
up and coming models

Industry/Entity Type

Photographer

Number of Pages Required

3 page

Requirements
Must have
• Home
• About me
• Contact me
• Portfolio or gallery

```html
<!DOCTYPE html>
<html lang="en">
<head>
<meta charset="utf-8">
<title>Marvento Quillas — Photographer</title>
<link rel="stylesheet" href="https://fonts.googleapis.com/css2?family=Oswald:wght@400;500&family=Playfair+Display:wght@400;700&display=swap">
<style>
  :root {
    --backdrop: #2b2a2a;
    --white: #ffffff;
    --paper: #f4f4f4;
    --ink: #2a2a2a;
    --muted: #8a8a8a;
    --rule: #d8d8d8;
    --dark: #121212;
    --black: #050505;
    --light-text: #e6e6e6;
  }
  * { box-sizing: border-box; margin: 0; padding: 0; }
  html, body { width: 1200px; height: 1200px; overflow: hidden; background: var(--backdrop); }
  body { font-family: "Playfair Display", serif; color: var(--ink); }
  .page { position: absolute; left: 438px; top: 0; width: 325px; height: 1200px; background: var(--white); overflow: hidden; }
  .abs { position: absolute; }
  .center { left: 0; width: 325px; text-align: center; }

  /* header */
  .site-header { top: 0; left: 0; width: 325px; height: 30px; background: var(--white); }
  .brand { left: 22px; top: 10px; font-size: 8px; font-weight: 400; color: var(--ink); letter-spacing: .2px; }
  .main-nav { left: 138px; top: 13px; display: flex; gap: 11px; font-family: "Oswald", sans-serif; font-size: 3.6px; color: var(--ink); letter-spacing: .1px; }
  .main-nav .active { color: var(--muted); }
  .nav-divider { left: 267px; top: 11px; width: 1px; height: 9px; background: var(--rule); }
  .social { display: flex; gap: 4px; }
  .social span { width: 4px; height: 4px; border-radius: 50%; background: currentColor; display: block; }
  .header-social { left: 271px; top: 14px; color: var(--ink); }

  /* hero */
  .hero { top: 30px; left: 0; width: 325px; height: 132px; background: linear-gradient(100deg, #3d3a33 0%, #6b665a 35%, #8a8370 55%, #5b5a50 78%, #2d3a4a 90%, #1f2a38 100%); }
  .hero-title { top: 54px; font-family: "Oswald", sans-serif; font-size: 17px; line-height: 22px; color: var(--white); letter-spacing: -.2px; }
  .hero-arrow { top: 63px; }

  /* section titles */
  .sec-title { font-size: 5.2px; letter-spacing: .3px; text-transform: uppercase; display: flex; justify-content: center; align-items: center; gap: 4px; }
  .sec-title::before, .sec-title::after { content: ""; width: 18px; height: 2px; border-top: 1px solid currentColor; border-bottom: 1px solid currentColor; opacity: .35; }

  /* intro */
  .intro-heading { top: 170px; font-size: 9px; color: var(--ink); }
  .intro-sub { top: 183px; font-size: 4.3px; color: #555; }
  .specialties-title { top: 203px; color: var(--ink); }
  .spec-card { top: 213px; width: 90px; height: 86px; border: 1px solid #e6e6e6; background: var(--white); text-align: center; }
  .spec-card .photo { margin: 3px 4px 0; height: 54px; }
  .spec-card h3 { font-size: 6px; font-weight: 400; margin-top: 5px; color: var(--ink); }
  .spec-card p { font-size: 2.9px; line-height: 5px; color: var(--muted); margin-top: 2px; }

  /* latest shots grid */
  .shots-section { top: 315px; left: 0; width: 325px; height: 238px; background: var(--dark); }
  .shots-title { top: 14px; color: var(--light-text); }
  .shots-sub { top: 26px; font-size: 2.9px; color: #aaa; }
  .shot-grid { top: 40px; left: 0; width: 325px; height: 161px; display: grid; grid-template-columns: repeat(4, 1fr); grid-template-rows: repeat(3, 1fr); }
  .btn-outline { top: 213px; left: 143px; width: 38px; height: 10px; border: 1px solid #bbb; font-size: 2.6px; color: #ddd; text-align: center; line-height: 8px; letter-spacing: .2px; }

  /* journal */
  .journal { top: 553px; left: 0; width: 325px; height: 150px; background: var(--paper); }
  .journal-title { top: 12px; color: var(--ink); }
  .post-card { top: 28px; width: 90px; height: 113px; background: var(--white); border: 1px solid #e8e8e8; text-align: center; }
  .post-card h4 { font-size: 4.3px; font-weight: 700; margin-top: 7px; }
  .post-card .meta { font-size: 2.6px; color: var(--muted); margin-top: 1px; }
  .post-card .photo { height: 54px; margin-top: 5px; }
  .post-card p { font-size: 2.9px; line-height: 5px; text-align: left; color: var(--muted); padding: 6px 7px 0; }
  .post-card .foot { display: flex; justify-content: space-between; font-size: 2.2px; color: var(--muted); padding: 5px 7px 0; letter-spacing: .2px; }

  /* testimonial */
  .testimonial { top: 703px; left: 0; width: 325px; height: 75px; background: radial-gradient(circle at 62% 40%, #8a7a62 0%, #4a4236 18%, #1f1d1a 40%, #111 70%); }
  .testi-title { top: 10px; color: var(--light-text); }
  .testi-text { top: 31px; font-size: 4.2px; line-height: 6.5px; color: #ddd; }
  .testi-name { top: 48px; font-size: 3.6px; letter-spacing: .3px; color: #eee; }
  .dots { display: flex; justify-content: center; gap: 2px; }
  .dots span { width: 2px; height: 2px; border-radius: 50%; background: #999; display: block; }
  .dots span.on { background: #fff; }

  /* services */
  .services { top: 778px; left: 0; width: 325px; height: 94px; background: var(--white); }
  .services-title { top: 8px; color: var(--ink); }
  .service { width: 92px; display: flex; gap: 4px; }
  .service svg { flex: none; width: 12px; height: 12px; }
  .service h5 { font-size: 4.1px; font-weight: 700; margin-top: 1px; }
  .service p { font-size: 2.9px; line-height: 5px; color: var(--muted); margin-top: 3px; }

  /* latest shots strip */
  .strip { top: 872px; left: 0; width: 325px; height: 140px; background: var(--dark); }
  .strip-title { top: 15px; color: var(--light-text); }
  .strip-photo { top: 36px; width: 74px; height: 74px; }

  /* about */
  .about { top: 1012px; left: 0; width: 325px; height: 144px; background: var(--paper); }
  .about-title { left: 22px; top: 14px; font-size: 5.2px; letter-spacing: .2px; display: flex; align-items: center; gap: 4px; }
  .about-title::after { content: ""; width: 18px; border-top: 1px solid var(--rule); }
  .about-photo { left: 22px; top: 30px; width: 109px; height: 98px; }
  .about-heading { left: 142px; top: 33px; font-size: 6.6px; line-height: 13px; font-weight: 700; color: var(--ink); }
  .about-text { left: 142px; top: 70px; width: 150px; font-size: 4.1px; line-height: 7px; color: var(--muted); }

  /* footer */
  .site-footer { top: 1156px; left: 0; width: 325px; height: 44px; background: var(--black); }
  .footer-nav { top: 11px; display: flex; justify-content: center; gap: 14px; font-family: "Oswald", sans-serif; font-size: 3.4px; color: #ddd; }
  .copyright { top: 21px; font-size: 3px; color: #bbb; }
  .footer-social { top: 30px; justify-content: center; color: #ccc; }
</style>
</head>
<body>
<div class="page">

  <header class="site-header abs">
    <div class="brand abs">marvento quillas</div>
    <nav class="main-nav abs">
      <span class="active">HOME</span><span>ABOUT ME</span><span>PORTFOLIO</span><span>GALLERY</span><span>CONTACT ME</span>
    </nav>
    <div class="nav-divider abs"></div>
    <div class="social header-social abs"><span></span><span></span><span></span><span></span></div>
  </header>

  <section class="hero abs" role="img" aria-label="Vintage bicycle leaning on a stone wall with a basket of flowers">
    <svg class="hero-arrow abs" style="left:7px" width="6" height="12" viewBox="0 0 6 12"><path d="M5 1 L1 6 L5 11" fill="none" stroke="#fff" stroke-width="1"/></svg>
    <svg class="hero-arrow abs" style="left:312px" width="6" height="12" viewBox="0 0 6 12"><path d="M1 1 L5 6 L1 11" fill="none" stroke="#fff" stroke-width="1"/></svg>
    <h1 class="hero-title abs center">LOREM IPSUM DOLOR<br>SIT AMET CONSEC</h1>
  </section>

  <h2 class="intro-heading abs center" style="font-weight:400">Hello! I'm Marvento Quillas ipsum dolor sit amet</h2>
  <p class="intro-sub abs center">Lorem ipsum dolor sit amet consectetur adipiscing</p>
  <div class="specialties-title sec-title abs center">My Specialties</div>

  <article class="spec-card abs" style="left:22px">
    <div class="photo" role="img" aria-label="Woman standing in a tall grass field" style="background:linear-gradient(160deg,#c8c29a,#7d7a4a 50%,#4b4a2c)"></div>
    <h3>Landscape</h3>
    <p>Lorem ipsum dolor sit amet, consectetur adipisci<br>Aliquam venenatis nibh vitae consequa.</p>
  </article>
  <article class="spec-card abs" style="left:119px">
    <div class="photo" role="img" aria-label="Lit lighter against a teal sky" style="background:linear-gradient(180deg,#3fa7c4,#6cc5d6 55%,#c9a58a 80%,#2b3a40)"></div>
    <h3>Advertorial</h3>
    <p>Lorem ipsum dolor sit amet, consectetur adipisci<br>Aliquam venenatis nibh vitae consequa.</p>
  </article>
  <article class="spec-card abs" style="left:216px">
    <div class="photo" role="img" aria-label="Woman holding red roses in a dark setting" style="background:linear-gradient(170deg,#4a4a4a,#7a2a2c 45%,#2a2a2a)"></div>
    <h3>Conceptual</h3>
    <p>Lorem ipsum dolor sit amet, consectetur adipisci<br>Aliquam venenatis nibh vitae consequa.</p>
  </article>

  <section class="shots-section abs">
    <div class="shots-title sec-title abs center">My Latest Shots</div>
    <p class="shots-sub abs center">Lorem ipsum dolor sit amet consectetur adipiscing elit Aliquam venenatis sed in amet consectetur adipiscing elit Aliquam</p>
    <div class="shot-grid abs">
      <div role="img" aria-label="Woman in a misty forest" style="background:linear-gradient(160deg,#8d8f8c,#4a4b48)"></div>
      <div role="img" aria-label="Close-up of a worn boot" style="background:linear-gradient(160deg,#3a2a22,#a8674a 50%,#2a1c16)"></div>
      <div role="img" aria-label="Ladybird on a turquoise background" style="background:radial-gradient(circle at 40% 60%,#7fd8d8,#2aa0a8 60%,#11707a)"></div>
      <div role="img" aria-label="Glowing butterflies at night" style="background:radial-gradient(circle at 60% 40%,#5a4a2a,#1c1a14 60%)"></div>
      <div role="img" aria-label="Colourful balloons" style="background:linear-gradient(135deg,#e2b02a,#4fa84f 40%,#d04a5a 70%,#2a7ac0)"></div>
      <div role="img" aria-label="Branches with teal bokeh lights" style="background:radial-gradient(circle at 50% 50%,#3f7a84,#1a2a34 70%)"></div>
      <div role="img" aria-label="Narrow golden street at dusk" style="background:linear-gradient(180deg,#b28a3a,#6a5030 50%,#2a2a22)"></div>
      <div role="img" aria-label="Person walking on a path" style="background:linear-gradient(160deg,#c89a6a,#6a4a30 60%,#3a2a1c)"></div>
      <div role="img" aria-label="Blossoming trees over a green path" style="background:linear-gradient(180deg,#c98a9a,#7a6a5a 45%,#3a8a3a)"></div>
      <div role="img" aria-label="Woman in a blue dress" style="background:linear-gradient(160deg,#2a6a8a,#7a9aa8 50%,#c8a860)"></div>
      <div role="img" aria-label="Paper hearts on a string" style="background:linear-gradient(160deg,#7ac070,#3a8a4a 60%,#1a4a2a)"></div>
      <div role="img" aria-label="Abandoned railway track" style="background:linear-gradient(170deg,#8a8a80,#4a4a40 50%,#2a2a24)"></div>
    </div>
    <div class="btn-outline abs">SEE PORTFOLIO</div>
  </section>

  <section class="journal abs">
    <div class="journal-title sec-title abs center">From the Journal</div>
    <article class="post-card abs" style="left:22px">
      <h4>Lorem ipsum dolor sit amet nibu</h4>
      <div class="meta">18.04.2014 Photography, Journal</div>
      <div class="photo" role="img" aria-label="Woman among yellow spring flowers" style="background:linear-gradient(160deg,#7ab0c8,#8aa85a 50%,#d8c84a)"></div>
      <p>Lorem ipsum dolor sit amet, consectetur adipisci Aliquam venenatis nibh vitae consequa. amet, consectetur adipisci</p>
      <div class="foot"><span>CONTINUE READING</span><span>17.10</span></div>
    </article>
    <article class="post-card abs" style="left:119px">
      <h4>Lorem ipsum dolor sit amet nibu</h4>
      <div class="meta">18.04.2014 Photography, Journal</div>
      <div class="photo" role="img" aria-label="Pink roses in a basket on a table" style="background:linear-gradient(160deg,#3a4a3a,#d86a7a 45%,#8a6a5a)"></div>
      <p>Lorem ipsum dolor sit amet, consectetur adipisci Aliquam venenatis nibh vitae consequa. amet, consectetur adipisci</p>
      <div class="foot"><span>CONTINUE READING</span><span>17.10</span></div>
    </article>
    <article class="post-card abs" style="left:216px">
      <h4>Lorem ipsum dolor sit amet nibu</h4>
      <div class="meta">18.04.2014 Photography, Journal</div>
      <div class="photo" role="img" aria-label="Red scooter parked on a street" style="background:linear-gradient(160deg,#c8c0a0,#8a9a7a 45%,#b8282a 70%,#5a5a5a)"></div>
      <p>Lorem ipsum dolor sit amet, consectetur adipisci Aliquam venenatis nibh vitae consequa. amet, consectetur adipisci</p>
      <div class="foot"><span>CONTINUE READING</span><span>17.10</span></div>
    </article>
  </section>

  <section class="testimonial abs" role="img" aria-label="Close-up of a vintage camera lens">
    <div class="testi-title sec-title abs center">Customer Testimonials</div>
    <p class="testi-text abs center">Lorem ipsum dolor sit amet consectetur adipiscing elit Aliquam venenatis nibh vitae<br>nam sed lorem tristique nisl egestas sollicitudin lorem ipsum</p>
    <div class="testi-name abs center">DORIN PELHAM</div>
    <div class="dots abs center" style="top:65px"><span class="on"></span><span></span><span></span></div>
  </section>

  <section class="services abs">
    <div class="services-title sec-title abs center">My Services</div>

    <div class="service abs" style="left:22px;top:27px">
      <svg viewBox="0 0 12 12"><path d="M6 10 L1.5 5.5 A2.3 2.3 0 0 1 6 3 A2.3 2.3 0 0 1 10.5 5.5 Z" fill="none" stroke="#666" stroke-width=".6"/></svg>
      <div><h5>Wedding Photography</h5><p>Lorem ipsum dolor sit amet, consectetur adipisci<br>Aliquam venenatis nibh vitae consequa<br>amet,consectetur adipisci</p></div>
    </div>
    <div class="service abs" style="left:117px;top:27px">
      <svg viewBox="0 0 12 12"><path d="M2 2 H10 L6 6.5 Z M6 6.5 V10 M4 10 H8" fill="none" stroke="#666" stroke-width=".6"/></svg>
      <div><h5>Drink Photography</h5><p>Lorem ipsum dolor sit amet, consectetur adipisci<br>Aliquam venenatis nibh vitae consequa<br>amet,consectetur adipisci</p></div>
    </div>
    <div class="service abs" style="left:213px;top:27px">
      <svg viewBox="0 0 12 12"><path d="M2 5 H10 V10.5 H2 Z M1.5 3.5 H10.5 V5 H1.5 Z M6 3.5 V10.5" fill="none" stroke="#666" stroke-width=".6"/></svg>
      <div><h5>Birth Photography</h5><p>Lorem ipsum dolor sit amet, consectetur adipisci<br>Aliquam venenatis nibh vitae consequa<br>amet,consectetur adipisci</p></div>
    </div>
    <div class="service abs" style="left:22px;top:60px">
      <svg viewBox="0 0 12 12"><path d="M1.5 4 H10.5 V10 H1.5 Z M4.5 4 V2.5 H7.5 V4 M1.5 6.5 H10.5" fill="none" stroke="#666" stroke-width=".6"/></svg>
      <div><h5>Fashion Photography</h5><p>Lorem ipsum dolor sit amet, consectetur adipisci<br>Aliquam venenatis nibh vitae consequa<br>amet,consectetur adipisci</p></div>
    </div>
    <div class="service abs" style="left:117px;top:60px">
      <svg viewBox="0 0 12 12"><circle cx="6" cy="6" r="4.5" fill="none" stroke="#666" stroke-width=".6"/><circle cx="6" cy="6" r="2.8" fill="none" stroke="#666" stroke-width=".6"/></svg>
      <div><h5>Food Photography</h5><p>Lorem ipsum dolor sit amet, consectetur adipisci<br>Aliquam venenatis nibh vitae consequa<br>amet,consectetur adipisci</p></div>
    </div>
    <div class="service abs" style="left:213px;top:60px">
      <svg viewBox="0 0 12 12"><path d="M1.5 4.5 L3.5 2 H8.5 L10.5 4.5 L6 10.5 Z M1.5 4.5 H10.5" fill="none" stroke="#666" stroke-width=".6"/></svg>
      <div><h5>Jewelry Photography</h5><p>Lorem ipsum dolor sit amet, consectetur adipisci<br>Aliquam venenatis nibh vitae consequa<br>amet,consectetur adipisci</p></div>
    </div>
  </section>

  <section class="strip abs">
    <div class="strip-title sec-title abs center">Latest Shots</div>
    <div class="strip-photo abs" style="left:6px" role="img" aria-label="Pink roses beside a pocket watch" style="background:#999"></div>
    <div class="strip-photo abs" style="left:6px;background:linear-gradient(160deg,#d8d8d8,#c088a8 45%,#5a5a5a)" role="img" aria-label="Pink roses beside a pocket watch"></div>
    <div class="strip-photo abs" style="left:85px;background:linear-gradient(180deg,#3a3a3a,#c88a4a 45%,#e8e8e8 75%,#2a2a2a)" role="img" aria-label="Bride and groom at sunset"></div>
    <div class="strip-photo abs" style="left:164px;background:linear-gradient(160deg,#6a8a9a,#b02a2a 50%,#3a4a5a)" role="img" aria-label="Woman in a red dress on a bench"></div>
    <div class="strip-photo abs" style="left:244px;background:linear-gradient(160deg,#8a8a5a,#c8c0a8 50%,#6a6a4a)" role="img" aria-label="Young girl in a white coat"></div>
    <div class="dots abs center" style="top:125px"><span class="on"></span><span></span><span></span></div>
  </section>

  <section class="about abs">
    <div class="about-title abs">A LITTLE ABOUT ME</div>
    <div class="about-photo abs" role="img" aria-label="Portrait of the photographer holding a camera" style="background:linear-gradient(150deg,#9a9a98,#5a5a5c 50%,#1f2a3a)"></div>
    <h2 class="about-heading abs">Cras mattis consectetur purus sitor amet<br>sed donec malesuada odio.</h2>
    <p class="about-text abs">Lorem ipsum dolor sit amet, consectetur adipiscing elit. Aliquam venenatis nibh vitae consequat auctor. Aliquam sed lorem tristiq nisl egestas sollicitudin. Duis pulvinar vitae purus sed luctus. Nulla aliquet, ligula nec dapibus tristique, sapien mauris effi citur elit, vitae volutpat ipsum libero in leo. Fusce ac nisi purus. Nullam finibus elit at ex interdum molestie. Etiam et leo nisl. Duis accumsan.</p>
  </section>

  <footer class="site-footer abs">
    <nav class="footer-nav abs center"><span>HOME</span><span>ABOUT ME</span><span>PORTFOLIO</span><span>GALLERY</span><span>CONTACT ME</span></nav>
    <p class="copyright abs center">Copyright ©. All Rights Reserved</p>
    <div class="social footer-social abs center"><span></span><span></span><span></span><span></span><span></span><span></span></div>
  </footer>

</div>
</body>
</html>
```